Update our business cards to match our awesome new website

Need a new design for company business cards. We have recently revamped our website and would like our business cards to get a refresh too. I've uploaded the company artwork, logo, as well as the Branding Deck to better understand the look & feel of our brand. Please visit the website at bellcrestholdingsoh.com.

Industry/Entity Type

Real Estate

Contact Information for Business Card

must use the colors outlined in the Branding Deck uploaded to the site, or the colors of our logo.

Font styles to use
Other font styles liked:
• Calibri

Requirements
Must have
• Required items: Name, title, company logo, address: 217 Fennimore Ave. Suite 300, Lakeport, OH 44093, email address: glen@bellcrestholdingsOH.com, company phone 800-555-0172, cell: 216-555-0148
Nice to have
• a more simple design. not complicated
Should not have
• cartoonish characters, or whimsical writing or artwork, stay within our branding colors

```html
<!DOCTYPE html>
<html lang="en">
<head>
<meta charset="utf-8">
<title>Bellcrest Holdings – Business Card</title>
<link rel="stylesheet" href="https://fonts.googleapis.com/css2?family=Carlito:wght@400;700&display=swap">
<style>
  :root {
    --page-bg: #dcdcdc;
    --navy: #1c2d59;
    --green: #6cb33f;
    --white: #ffffff;
    --ink: #3a3a3a;
    --card-shadow: 0 14px 30px rgba(0,0,0,0.28);
  }
  * { box-sizing: border-box; margin: 0; padding: 0; }
  html, body { width: 1200px; height: 1200px; overflow: hidden; }
  body {
    background: var(--page-bg);
    font-family: "Carlito", "Calibri", sans-serif;
    position: relative;
  }
  .card {
    position: absolute;
    left: 204px;
    width: 792px;
    height: 460px;
    box-shadow: var(--card-shadow);
  }
  .card-front { top: 92px; background: var(--navy); }
  .card-back { top: 652px; background: var(--white); }

  /* Front */
  .brand {
    position: absolute;
    left: 0; right: 0; top: 150px;
    display: flex; flex-direction: column; align-items: center; gap: 18px;
  }
  .brand-dot {
    width: 64px; height: 64px; border-radius: 50%;
    background: var(--green);
  }
  .brand-name {
    color: var(--white);
    font-size: 44px;
    font-weight: 400;
    letter-spacing: 1px;
  }
  .social-list {
    position: absolute;
    left: 0; right: 0; top: 382px;
    display: flex; justify-content: center; gap: 22px;
    list-style: none;
  }
  .social-link {
    display: flex; align-items: center; gap: 7px;
    color: var(--green);
    font-size: 17px;
    font-weight: 700;
    line-height: 1;
  }
  .social-link::before {
    content: "";
    width: 14px; height: 14px; border-radius: 50%;
    background: var(--green);
  }

  /* Back */
  .person {
    position: absolute;
    right: 452px; top: 214px;
    text-align: right;
  }
  .person-name {
    color: var(--green);
    font-size: 27px;
    font-weight: 700;
    line-height: 1;
  }
  .person-title {
    color: var(--ink);
    font-size: 18px;
    margin-top: 5px;
  }
  .divider {
    position: absolute;
    left: 362px; top: 160px;
    width: 2px; height: 144px;
    background: var(--green);
  }
  .contact-list {
    position: absolute;
    left: 384px; top: 162px;
    list-style: none;
    color: var(--ink);
    font-size: 15px;
    line-height: 22px;
  }
  .contact-list li { display: flex; align-items: flex-start; }
  .contact-icon {
    width: 16px; height: 16px; margin: 3px 13px 0 0; flex: none;
    fill: none; stroke: var(--green); stroke-width: 1.8;
  }
  .contact-list .continued { padding-left: 29px; }
</style>
</head>
<body>
  <section class="card card-front">
    <div class="brand">
      <span class="brand-dot"></span>
      <span class="brand-name">Bellcrest Holdings of Ohio, LLC</span>
    </div>
    <ul class="social-list" aria-label="Social links">
      <li class="social-link">Worklane</li>
      <li class="social-link">Circlo</li>
      <li class="social-link">Chirpwire</li>
      <li class="social-link">Vidstream</li>
    </ul>
  </section>

  <section class="card card-back">
    <div class="person">
      <p class="person-name">Glen Harwick</p>
      <p class="person-title">Managing Member</p>
    </div>
    <div class="divider"></div>
    <ul class="contact-list">
      <li>
        <svg class="contact-icon" viewBox="0 0 18 18"><rect x="5" y="1.5" width="8" height="15" rx="1.5"/><line x1="8" y1="14" x2="10" y2="14"/></svg>
        216-555-0148
      </li>
      <li>
        <svg class="contact-icon" viewBox="0 0 18 18"><path d="M2 7c0-3 3-4 7-4s7 1 7 4l-3 1-1-2H6L5 8z"/><rect x="4" y="9" width="10" height="6" rx="1"/></svg>
        800-555-0172
      </li>
      <li>
        <svg class="contact-icon" viewBox="0 0 18 18"><rect x="1.5" y="4" width="15" height="10" rx="1"/><path d="M1.5 4.5 9 10l7.5-5.5"/></svg>
        glen@bellcrestholdingsOH.com
      </li>
      <li>
        <svg class="contact-icon" viewBox="0 0 18 18"><circle cx="9" cy="9" r="7"/><ellipse cx="9" cy="9" rx="3" ry="7"/><line x1="2" y1="9" x2="16" y2="9"/></svg>
        bellcrestholdingsoh.com
      </li>
      <li>
        <svg class="contact-icon" viewBox="0 0 18 18"><path d="M9 16.5s-5-5.5-5-9a5 5 0 0 1 10 0c0 3.5-5 9-5 9z"/><circle cx="9" cy="7.5" r="1.8"/></svg>
        217 Fennimore Ave. Suite 300,
      </li>
      <li class="continued">Lakeport, OH 44093</li>
    </ul>
  </section>
</body>
</html>
```